Patient Fact sheets for medical conditions and treatments

Hi,

I need a new design for my patient fact sheets. I am moving from my current clinic and I am looking from a new look.

I have attached
1. a current Fact sheet
2. New home page to the website
3. New Logo.

They need to be single page and easily readable for patients.

The will be in both PDF and print form in the future.

Target Market(s)

Patients with chronic pain age 40+

Font styles to use
Serif

Requirements
Must have
• My logo, should be inline with design elements on the Front page provided.

Please use the same font as the Logo

```html
<!DOCTYPE html>
<html lang="en">
<head>
<meta charset="utf-8">
<title>Patient Fact Sheet – Design Options</title>
<link href="https://fonts.googleapis.com/css2?family=Cinzel:wght@500&family=Open+Sans:wght@600;700&family=Raleway:wght@500;700&display=swap" rel="stylesheet">
<style>
:root{
  --bg-light:#202022;
  --bg-dark:#141416;
  --grey:#9a9b9e;
  --navy:#2f2c80;
  --teal:#1ba2b6;
  --ink:#333335;
  --body:#5a5a5c;
  --white:#ffffff;
}
*{box-sizing:border-box;margin:0;padding:0}
html,body{width:1200px;height:868px;overflow:hidden;background:var(--bg-dark)}
.board{position:relative;width:1200px;height:868px;overflow:hidden}
.board-bg{position:absolute;inset:0}
.option-label{position:absolute;width:300px;margin-left:-150px;text-align:center;font-family:"Open Sans",sans-serif;font-weight:700;font-size:25px;line-height:30px;color:var(--white)}
.sheet{position:absolute;width:214px;height:301px;background:var(--white);overflow:hidden}
.theme-1{--head:var(--grey);--swoosh:var(--grey);--stripe:var(--navy)}
.theme-2{--head:var(--navy);--swoosh:var(--grey);--stripe:var(--navy)}
.theme-3{--head:var(--navy);--swoosh:var(--navy);--stripe:var(--grey)}
.theme-4{--head:var(--grey);--swoosh:var(--navy);--stripe:var(--grey)}
.sheet-shapes{position:absolute;inset:0}
.shape-head{fill:var(--head)}
.shape-swoosh{fill:var(--swoosh)}
.shape-stripe{fill:var(--stripe)}
.social-dot{fill:var(--swoosh);stroke:var(--white);stroke-width:1.3}
.fact-title{position:absolute;left:16px;top:12px;font-family:"Open Sans",sans-serif;font-weight:600;font-size:19px;line-height:17px;color:var(--white)}
.brand-name{position:absolute;right:11px;top:27px;text-align:right;font-family:"Cinzel",serif;font-weight:500;font-size:6.6px;line-height:7.6px;color:var(--ink)}
.treatment-title{position:absolute;right:143px;top:77px;text-align:right;font-family:"Raleway",sans-serif;font-weight:700;font-size:10px;line-height:13px;color:var(--teal)}
.treatment-title .last{display:block;margin-top:4px}
.hero-photo{position:absolute;left:78px;top:68px;width:124px;height:74px;background:linear-gradient(120deg,#e4e7eb 0%,#cdd2d8 45%,#d9cf8f 62%,#e6e8eb 100%)}
.content{position:absolute;left:12px;font-family:"Raleway",sans-serif}
.content-front{top:157px;width:190px}
.content-back{top:91px;width:196px}
.content h2{font-weight:700;font-size:5.6px;line-height:7px;color:var(--teal);margin:0 0 1.5px}
.content p{font-weight:500;font-size:3.1px;line-height:4.3px;color:var(--body);text-align:justify;margin:0 0 3px}
.content .section{margin-bottom:6px}
.content ul{list-style:none;font-weight:500;font-size:3.1px;line-height:4.3px;color:var(--body);margin:0 0 3px}
.content li::before{content:"• "}
.treat-list{width:60px}
.treat-list p{text-align:left}
.contact{position:absolute;right:12px;top:264px;text-align:right;font-family:"Raleway",sans-serif;font-weight:500;font-size:3.4px;line-height:4.5px;color:var(--white)}
.contact strong{font-weight:700}
</style>
</head>
<body>
<main class="board">
  <svg class="board-bg" width="1200" height="868" viewBox="0 0 1200 868" aria-hidden="true">
    <rect width="1200" height="868" fill="var(--bg-dark)"/>
    <polygon points="0,0 1165,0 0,800" fill="var(--bg-light)"/>
  </svg>

  <div class="option-label" style="left:342px;top:50px">Option-01</div>
  <div class="option-label" style="left:858px;top:50px">Option-02</div>
  <div class="option-label" style="left:342px;top:786px">Option-03</div>
  <div class="option-label" style="left:858px;top:786px">Option-04</div>

  <!-- OPTION 1 -->
  <article class="sheet sheet-front theme-1" style="left:118px;top:102px">
    <svg class="sheet-shapes" width="214" height="301" viewBox="0 0 214 301" aria-hidden="true">
      <path class="shape-head" d="M0 0H214V19H118C95 19 88 40 75 50C66 57 60 60 50 60H0Z"/>
      <path class="shape-stripe" d="M0 293C40 291 80 291 102 297L112 301H0Z"/>
      <path class="shape-swoosh" d="M100 301C118 301 122 270 140 262C146 259.5 152 259 160 259H214V301Z"/>
      <circle class="social-dot" cx="19" cy="288" r="6.5"/><circle class="social-dot" cx="38" cy="288" r="6.5"/><circle class="social-dot" cx="57" cy="288" r="6.5"/>
    </svg>
    <div class="fact-title">FACT<br>SHEET</div>
    <div class="brand-name">Dr Ava Lund<br>Back &amp; Joint Care</div>
    <h1 class="treatment-title">Platelet<br>Rich Plasma<br>(PRP)<span class="last">Therapy</span></h1>
    <div class="hero-photo" role="img" aria-label="Photo of a gloved hand holding test tubes of yellow plasma"></div>
    <div class="content content-front">
      <div class="section"><h2>WHAT IS PRP?</h2>
        <p>Platelet rich plasma is a concentrate of platelets and white cells taken from a small sample of your own blood. It is a growing treatment option for soft tissue injury of tendon, muscle and ligament, and it shows good results for mild to moderate joint wear. It has been used overseas for many years.</p>
        <p>Platelets carry small granules that hold growth factors. When these are released they signal nearby repair cells to start work on the injured area. In a sore tendon, for example, the treated site is prompted to lay down fresh tissue and strengthen the weak region. White cells also help clear away tissue that has been damaged over time, easing pain and thickening in the area.</p></div>
      <div class="section"><h2>HOW DOES PRP WORK?</h2>
        <p>Some tissues have a poor blood supply or respond poorly to load, so they struggle to heal on their own. Physiotherapy, massage and exercise help many people, yet some injuries still fail to settle. PRP uses the healing power of your blood to start repair in tissue that has not healed.</p></div>
    </div>
    <div class="contact"><strong>FOR MORE INFORMATION:</strong><br>DR AVA LUND | BACK &amp; JOINT CARE<br>Harbour House, Ground Floor<br>48 Elm Road, Northvale VIC 3999<br>T 03 9000 1200 | F 03 9000 1201<br>E hello@backjointcare.example</div>
  </article>

  <article class="sheet sheet-back theme-1" style="left:352px;top:102px">
    <svg class="sheet-shapes" width="214" height="301" viewBox="0 0 214 301" aria-hidden="true">
      <path class="shape-head" d="M0 0H214V19H118C95 19 88 40 75 50C66 57 60 60 50 60H0Z"/>
      <path class="shape-stripe" d="M0 293C40 291 80 291 102 297L112 301H0Z"/>
      <path class="shape-swoosh" d="M100 301C118 301 122 270 140 262C146 259.5 152 259 160 259H214V301Z"/>
      <circle class="social-dot" cx="19" cy="288" r="6.5"/><circle class="social-dot" cx="38" cy="288" r="6.5"/><circle class="social-dot" cx="57" cy="288" r="6.5"/>
    </svg>
    <div class="fact-title">FACT<br>SHEET</div>
    <div class="brand-name">Dr Ava Lund<br>Back &amp; Joint Care</div>
    <div class="content content-back">
      <div class="section"><h2>ROLE OF PLATELETS &amp; GROWTH FACTORS</h2>
        <p>PRP holds a high level of platelets. These release growth factors that are known to play a role in:</p>
        <ul><li>raising blood flow to tissue and speeding surface repair (wound healing)</li><li>drawing in other cells that fight infection</li><li>acting as a seal during closure to reduce bleeding</li><li>bone growth and repair</li></ul></div>
      <div class="section"><h2>WHAT ARE THE EXPECTED RESULTS OF PRP?</h2>
        <p>Because PRP aims to ease pain through healing, results can last. Early change may be seen within a few weeks, with steady gains as healing goes on. Studies and clinic use show PRP can relieve pain and help patients return to normal life. The need for surgery may also fall when tissue is treated early.</p></div>
      <div class="section treat-list"><h2>WHAT CAN PRP TREAT?</h2>
        <p>PRP therapy can be used for:</p>
        <ul><li>orthopaedic surgery</li><li>heart surgery</li><li>plastic and cosmetic surgery</li><li>ear, nose and throat surgery</li><li>oral and facial surgery</li><li>nerve surgery</li><li>vascular surgery</li><li>wound healing</li><li>burn care</li></ul>
        <p>Ask your doctor whether PRP is suitable for your procedure</p></div>
    </div>
    <div class="contact"><strong>FOR MORE INFORMATION:</strong><br>DR AVA LUND | BACK &amp; JOINT CARE<br>Harbour House, Ground Floor<br>48 Elm Road, Northvale VIC 3999<br>T 03 9000 1200 | F 03 9000 1201<br>E hello@backjointcare.example</div>
  </article>

  <!-- OPTION 2 -->
  <article class="sheet sheet-front theme-2" style="left:634px;top:102px">
    <svg class="sheet-shapes" width="214" height="301" viewBox="0 0 214 301" aria-hidden="true">
      <path class="shape-head" d="M0 0H214V19H118C95 19 88 40 75 50C66 57 60 60 50 60H0Z"/>
      <path class="shape-stripe" d="M0 293C40 291 80 291 102 297L112 301H0Z"/>
      <path class="shape-swoosh" d="M100 301C118 301 122 270 140 262C146 259.5 152 259 160 259H214V301Z"/>
      <circle class="social-dot" cx="19" cy="288" r="6.5"/><circle class="social-dot" cx="38" cy="288" r="6.5"/><circle class="social-dot" cx="57" cy="288" r="6.5"/>
    </svg>
    <div class="fact-title">FACT<br>SHEET</div>
    <div class="brand-name">Dr Ava Lund<br>Back &amp; Joint Care</div>
    <h1 class="treatment-title">Platelet<br>Rich Plasma<br>(PRP)<span class="last">Therapy</span></h1>
    <div class="hero-photo" role="img" aria-label="Photo of a gloved hand holding test tubes of yellow plasma"></div>
    <div class="content content-front">
      <div class="section"><h2>WHAT IS PRP?</h2>
        <p>Platelet rich plasma is a concentrate of platelets and white cells taken from a small sample of your own blood. It is a growing treatment option for soft tissue injury of tendon, muscle and ligament, and it shows good results for mild to moderate joint wear. It has been used overseas for many years.</p>
        <p>Platelets carry small granules that hold growth factors. When these are released they signal nearby repair cells to start work on the injured area. In a sore tendon, for example, the treated site is prompted to lay down fresh tissue and strengthen the weak region. White cells also help clear away tissue that has been damaged over time, easing pain and thickening in the area.</p></div>
      <div class="section"><h2>HOW DOES PRP WORK?</h2>
        <p>Some tissues have a poor blood supply or respond poorly to load, so they struggle to heal on their own. Physiotherapy, massage and exercise help many people, yet some injuries still fail to settle. PRP uses the healing power of your blood to start repair in tissue that has not healed.</p></div>
    </div>
    <div class="contact"><strong>FOR MORE INFORMATION:</strong><br>DR AVA LUND | BACK &amp; JOINT CARE<br>Harbour House, Ground Floor<br>48 Elm Road, Northvale VIC 3999<br>T 03 9000 1200 | F 03 9000 1201<br>E hello@backjointcare.example</div>
  </article>

  <article class="sheet sheet-back theme-2" style="left:869px;top:102px">
    <svg class="sheet-shapes" width="214" height="301" viewBox="0 0 214 301" aria-hidden="true">
      <path class="shape-head" d="M0 0H214V19H118C95 19 88 40 75 50C66 57 60 60 50 60H0Z"/>
      <path class="shape-stripe" d="M0 293C40 291 80 291 102 297L112 301H0Z"/>
      <path class="shape-swoosh" d="M100 301C118 301 122 270 140 262C146 259.5 152 259 160 259H214V301Z"/>
      <circle class="social-dot" cx="19" cy="288" r="6.5"/><circle class="social-dot" cx="38" cy="288" r="6.5"/><circle class="social-dot" cx="57" cy="288" r="6.5"/>
    </svg>
    <div class="fact-title">FACT<br>SHEET</div>
    <div class="brand-name">Dr Ava Lund<br>Back &amp; Joint Care</div>
    <div class="content content-back">
      <div class="section"><h2>ROLE OF PLATELETS &amp; GROWTH FACTORS</h2>
        <p>PRP holds a high level of platelets. These release growth factors that are known to play a role in:</p>
        <ul><li>raising blood flow to tissue and speeding surface repair (wound healing)</li><li>drawing in other cells that fight infection</li><li>acting as a seal during closure to reduce bleeding</li><li>bone growth and repair</li></ul></div>
      <div class="section"><h2>WHAT ARE THE EXPECTED RESULTS OF PRP?</h2>
        <p>Because PRP aims to ease pain through healing, results can last. Early change may be seen within a few weeks, with steady gains as healing goes on. Studies and clinic use show PRP can relieve pain and help patients return to normal life. The need for surgery may also fall when tissue is treated early.</p></div>
      <div class="section treat-list"><h2>WHAT CAN PRP TREAT?</h2>
        <p>PRP therapy can be used for:</p>
        <ul><li>orthopaedic surgery</li><li>heart surgery</li><li>plastic and cosmetic surgery</li><li>ear, nose and throat surgery</li><li>oral and facial surgery</li><li>nerve surgery</li><li>vascular surgery</li><li>wound healing</li><li>burn care</li></ul>
        <p>Ask your doctor whether PRP is suitable for your procedure</p></div>
    </div>
    <div class="contact"><strong>FOR MORE INFORMATION:</strong><br>DR AVA LUND | BACK &amp; JOINT CARE<br>Harbour House, Ground Floor<br>48 Elm Road, Northvale VIC 3999<br>T 03 9000 1200 | F 03 9000 1201<br>E hello@backjointcare.example</div>
  </article>

  <!-- OPTION 3 -->
  <article class="sheet sheet-front theme-3" style="left:118px;top:458px">
    <svg class="sheet-shapes" width="214" height="301" viewBox="0 0 214 301" aria-hidden="true">
      <path class="shape-head" d="M0 0H214V19H118C95 19 88 40 75 50C66 57 60 60 50 60H0Z"/>
      <path class="shape-stripe" d="M0 293C40 291 80 291 102 297L112 301H0Z"/>
      <path class="shape-swoosh" d="M100 301C118 301 122 270 140 262C146 259.5 152 259 160 259H214V301Z"/>
      <circle class="social-dot" cx="19" cy="288" r="6.5"/><circle class="social-dot" cx="38" cy="288" r="6.5"/><circle class="social-dot" cx="57" cy="288" r="6.5"/>
    </svg>
    <div class="fact-title">FACT<br>SHEET</div>
    <div class="brand-name">Dr Ava Lund<br>Back &amp; Joint Care</div>
    <h1 class="treatment-title">Platelet<br>Rich Plasma<br>(PRP)<span class="last">Therapy</span></h1>
    <div class="hero-photo" role="img" aria-label="Photo of a gloved hand holding test tubes of yellow plasma"></div>
    <div class="content content-front">
      <div class="section"><h2>WHAT IS PRP?</h2>
        <p>Platelet rich plasma is a concentrate of platelets and white cells taken from a small sample of your own blood. It is a growing treatment option for soft tissue injury of tendon, muscle and ligament, and it shows good results for mild to moderate joint wear. It has been used overseas for many years.</p>
        <p>Platelets carry small granules that hold growth factors. When these are released they signal nearby repair cells to start work on the injured area. In a sore tendon, for example, the treated site is prompted to lay down fresh tissue and strengthen the weak region. White cells also help clear away tissue that has been damaged over time, easing pain and thickening in the area.</p></div>
      <div class="section"><h2>HOW DOES PRP WORK?</h2>
        <p>Some tissues have a poor blood supply or respond poorly to load, so they struggle to heal on their own. Physiotherapy, massage and exercise help many people, yet some injuries still fail to settle. PRP uses the healing power of your blood to start repair in tissue that has not healed.</p></div>
    </div>
    <div class="contact"><strong>FOR MORE INFORMATION:</strong><br>DR AVA LUND | BACK &amp; JOINT CARE<br>Harbour House, Ground Floor<br>48 Elm Road, Northvale VIC 3999<br>T 03 9000 1200 | F 03 9000 1201<br>E hello@backjointcare.example</div>
  </article>

  <article class="sheet sheet-back theme-3" style="left:352px;top:458px">
    <svg class="sheet-shapes" width="214" height="301" viewBox="0 0 214 301" aria-hidden="true">
      <path class="shape-head" d="M0 0H214V19H118C95 19 88 40 75 50C66 57 60 60 50 60H0Z"/>
      <path class="shape-stripe" d="M0 293C40 291 80 291 102 297L112 301H0Z"/>
      <path class="shape-swoosh" d="M100 301C118 301 122 270 140 262C146 259.5 152 259 160 259H214V301Z"/>
      <circle class="social-dot" cx="19" cy="288" r="6.5"/><circle class="social-dot" cx="38" cy="288" r="6.5"/><circle class="social-dot" cx="57" cy="288" r="6.5"/>
    </svg>
    <div class="fact-title">FACT<br>SHEET</div>
    <div class="brand-name">Dr Ava Lund<br>Back &amp; Joint Care</div>
    <div class="content content-back">
      <div class="section"><h2>ROLE OF PLATELETS &amp; GROWTH FACTORS</h2>
        <p>PRP holds a high level of platelets. These release growth factors that are known to play a role in:</p>
        <ul><li>raising blood flow to tissue and speeding surface repair (wound healing)</li><li>drawing in other cells that fight infection</li><li>acting as a seal during closure to reduce bleeding</li><li>bone growth and repair</li></ul></div>
      <div class="section"><h2>WHAT ARE THE EXPECTED RESULTS OF PRP?</h2>
        <p>Because PRP aims to ease pain through healing, results can last. Early change may be seen within a few weeks, with steady gains as healing goes on. Studies and clinic use show PRP can relieve pain and help patients return to normal life. The need for surgery may also fall when tissue is treated early.</p></div>
      <div class="section treat-list"><h2>WHAT CAN PRP TREAT?</h2>
        <p>PRP therapy can be used for:</p>
        <ul><li>orthopaedic surgery</li><li>heart surgery</li><li>plastic and cosmetic surgery</li><li>ear, nose and throat surgery</li><li>oral and facial surgery</li><li>nerve surgery</li><li>vascular surgery</li><li>wound healing</li><li>burn care</li></ul>
        <p>Ask your doctor whether PRP is suitable for your procedure</p></div>
    </div>
    <div class="contact"><strong>FOR MORE INFORMATION:</strong><br>DR AVA LUND | BACK &amp; JOINT CARE<br>Harbour House, Ground Floor<br>48 Elm Road, Northvale VIC 3999<br>T 03 9000 1200 | F 03 9000 1201<br>E hello@backjointcare.example</div>
  </article>

  <!-- OPTION 4 -->
  <article class="sheet sheet-front theme-4" style="left:634px;top:458px">
    <svg class="sheet-shapes" width="214" height="301" viewBox="0 0 214 301" aria-hidden="true">
      <path class="shape-head" d="M0 0H214V19H118C95 19 88 40 75 50C66 57 60 60 50 60H0Z"/>
      <path class="shape-stripe" d="M0 293C40 291 80 291 102 297L112 301H0Z"/>
      <path class="shape-swoosh" d="M100 301C118 301 122 270 140 262C146 259.5 152 259 160 259H214V301Z"/>
      <circle class="social-dot" cx="19" cy="288" r="6.5"/><circle class="social-dot" cx="38" cy="288" r="6.5"/><circle class="social-dot" cx="57" cy="288" r="6.5"/>
    </svg>
    <div class="fact-title">FACT<br>SHEET</div>
    <div class="brand-name">Dr Ava Lund<br>Back &amp; Joint Care</div>
    <h1 class="treatment-title">Platelet<br>Rich Plasma<br>(PRP)<span class="last">Therapy</span></h1>
    <div class="hero-photo" role="img" aria-label="Photo of a gloved hand holding test tubes of yellow plasma"></div>
    <div class="content content-front">
      <div class="section"><h2>WHAT IS PRP?</h2>
        <p>Platelet rich plasma is a concentrate of platelets and white cells taken from a small sample of your own blood. It is a growing treatment option for soft tissue injury of tendon, muscle and ligament, and it shows good results for mild to moderate joint wear. It has been used overseas for many years.</p>
        <p>Platelets carry small granules that hold growth factors. When these are released they signal nearby repair cells to start work on the injured area. In a sore tendon, for example, the treated site is prompted to lay down fresh tissue and strengthen the weak region. White cells also help clear away tissue that has been damaged over time, easing pain and thickening in the area.</p></div>
      <div class="section"><h2>HOW DOES PRP WORK?</h2>
        <p>Some tissues have a poor blood supply or respond poorly to load, so they struggle to heal on their own. Physiotherapy, massage and exercise help many people, yet some injuries still fail to settle. PRP uses the healing power of your blood to start repair in tissue that has not healed.</p></div>
    </div>
    <div class="contact"><strong>FOR MORE INFORMATION:</strong><br>DR AVA LUND | BACK &amp; JOINT CARE<br>Harbour House, Ground Floor<br>48 Elm Road, Northvale VIC 3999<br>T 03 9000 1200 | F 03 9000 1201<br>E hello@backjointcare.example</div>
  </article>

  <article class="sheet sheet-back theme-4" style="left:869px;top:458px">
    <svg class="sheet-shapes" width="214" height="301" viewBox="0 0 214 301" aria-hidden="true">
      <path class="shape-head" d="M0 0H214V19H118C95 19 88 40 75 50C66 57 60 60 50 60H0Z"/>
      <path class="shape-stripe" d="M0 293C40 291 80 291 102 297L112 301H0Z"/>
      <path class="shape-swoosh" d="M100 301C118 301 122 270 140 262C146 259.5 152 259 160 259H214V301Z"/>
      <circle class="social-dot" cx="19" cy="288" r="6.5"/><circle class="social-dot" cx="38" cy="288" r="6.5"/><circle class="social-dot" cx="57" cy="288" r="6.5"/>
    </svg>
    <div class="fact-title">FACT<br>SHEET</div>
    <div class="brand-name">Dr Ava Lund<br>Back &amp; Joint Care</div>
    <div class="content content-back">
      <div class="section"><h2>ROLE OF PLATELETS &amp; GROWTH FACTORS</h2>
        <p>PRP holds a high level of platelets. These release growth factors that are known to play a role in:</p>
        <ul><li>raising blood flow to tissue and speeding surface repair (wound healing)</li><li>drawing in other cells that fight infection</li><li>acting as a seal during closure to reduce bleeding</li><li>bone growth and repair</li></ul></div>
      <div class="section"><h2>WHAT ARE THE EXPECTED RESULTS OF PRP?</h2>
        <p>Because PRP aims to ease pain through healing, results can last. Early change may be seen within a few weeks, with steady gains as healing goes on. Studies and clinic use show PRP can relieve pain and help patients return to normal life. The need for surgery may also fall when tissue is treated early.</p></div>
      <div class="section treat-list"><h2>WHAT CAN PRP TREAT?</h2>
        <p>PRP therapy can be used for:</p>
        <ul><li>orthopaedic surgery</li><li>heart surgery</li><li>plastic and cosmetic surgery</li><li>ear, nose and throat surgery</li><li>oral and facial surgery</li><li>nerve surgery</li><li>vascular surgery</li><li>wound healing</li><li>burn care</li></ul>
        <p>Ask your doctor whether PRP is suitable for your procedure</p></div>
    </div>
    <div class="contact"><strong>FOR MORE INFORMATION:</strong><br>DR AVA LUND | BACK &amp; JOINT CARE<br>Harbour House, Ground Floor<br>48 Elm Road, Northvale VIC 3999<br>T 03 9000 1200 | F 03 9000 1201<br>E hello@backjointcare.example</div>
  </article>
</main>
</body>
</html>
```